Orthopedist website

We need a web design for a relaunch of this website: http://www.gelenkfix.at/
This website is for a orthopedist. Please fell free to create a modern and clean layout. The currently used colours need not to be used in the new design.
The website should transport reliability so that patients will call or contact the doctor for a treatment.
A specially logo is not available.
Reason: We will get a new logo which should be integrated into the design.
Reason: Customer will get a new logo (is ready soon).
The target market are patients from salzburg / austria which have orthopedic problems (hand, feet, backbone)
Doctor

```html
<!DOCTYPE html>
<html lang="de">
<head>
<meta charset="utf-8">
<title>Orthopädie Dr.Berger</title>
<link href="https://fonts.googleapis.com/css2?family=Maven+Pro:wght@400;500;600;700&display=swap" rel="stylesheet">
<style>
:root{
  --navy:#0f2b5b;
  --navy-nav:#15356a;
  --navy-deep:#0b2350;
  --gold:#d99c0e;
  --gold-deep:#cd9106;
  --gold-field:#c68a04;
  --gold-line:#b27b04;
  --gold-light:#e0ab2c;
  --text:#5b5b5b;
  --panel:#ebebeb;
  --page:#f1f1f1;
  --white:#ffffff;
}
*{box-sizing:border-box;margin:0;padding:0}
html,body{width:1117px;height:1200px;overflow:hidden}
body{font-family:"Maven Pro",sans-serif;background:var(--page);position:relative;color:var(--text)}
.topline{position:absolute;left:0;top:0;width:1117px;height:2px;background:var(--gold)}
.header{position:absolute;left:0;top:2px;width:1117px;height:87px;background:var(--navy)}
.brand{position:absolute;left:140px;top:15px;color:var(--white);font-size:15px;font-weight:500;line-height:18.5px;letter-spacing:.3px}
.social{position:absolute;left:609px;top:33px;display:flex;gap:4px}
.social span{width:21px;height:21px;border-radius:50%;background:#2d4778}
.social span:first-child{background:var(--white)}
.call{position:absolute;left:702px;top:34px;font-size:16px;color:var(--white);font-weight:500}
.call em{font-style:normal;color:var(--gold);font-weight:400;margin-right:4px}
.login{position:absolute;left:912px;top:28px;width:64px;height:29px;background:var(--gold);color:var(--white);font-size:10px;font-weight:700;letter-spacing:.6px;text-align:center;line-height:29px}
.nav{position:absolute;left:0;top:89px;width:1117px;height:35px;background:var(--navy)}
.nav ul{list-style:none;position:absolute;left:140px;width:838px;height:35px;display:flex;background:var(--navy-nav)}
.nav li{flex:none;color:var(--white);font-size:11.5px;letter-spacing:.3px;line-height:35px;text-align:center;white-space:nowrap;border-right:1px solid #0f2b5b}
.nav li:last-child{border-right:0}
.nav li.active{color:var(--gold);background:#1c3f78}
.goldbar{position:absolute;left:0;top:124px;width:1117px;height:5px;background:var(--gold)}
.main{position:absolute;left:140px;top:129px;width:838px;height:976px;background:var(--white);box-shadow:0 0 4px rgba(0,0,0,.08)}
.hero{position:absolute;left:150px;top:138px;width:595px;height:316px;background:linear-gradient(120deg,#a9d3c7 0%,#e8d4c4 35%,#8e8d8c 60%,#efefef 85%,#fafafa 100%)}
.hero-card{position:absolute;left:150px;top:227px;width:269px;height:152px;background:rgba(24,56,106,.88);padding:14px 21px;color:var(--white)}
.hero-card h2{font-size:19px;font-weight:400;line-height:18px}
.hero-card h2 span{color:var(--gold)}
.hero-card p{font-size:9.5px;line-height:15.5px;margin-top:9px}
.hero-card a{display:block;color:var(--gold);font-size:9.5px;margin:3px 0 0 4px}
.welcome{position:absolute;left:158px;top:474px;width:586px}
.welcome h1{color:var(--gold);font-size:17px;font-weight:600;text-align:center;letter-spacing:.3px}
.welcome p{font-size:10px;line-height:17px;margin-top:10px}
.services-title{position:absolute;left:150px;top:607px;width:595px;text-align:center;color:var(--gold);font-size:17px;font-weight:600}
.services{position:absolute;left:178px;top:640px;width:556px;height:274px;border:2px solid var(--gold);border-radius:2px}
.arrow{position:absolute;top:763px}
.service{position:absolute;top:663px;width:222px}
.service .photo{height:119px;border:1px solid #ddd;padding:5px;background:#fff}
.service .photo div{width:100%;height:100%}
.service h3{font-size:12px;font-weight:700;color:var(--navy);margin-top:12px;letter-spacing:.3px}
.service p{font-size:10.5px;line-height:17px;margin-top:4px}
.service a{color:var(--gold);font-size:10.5px;display:block;margin-top:5px}
.about{position:absolute;left:157px;top:930px;width:384px}
.about h2{color:var(--gold);font-size:17px;font-weight:600}
.about p{font-size:10.5px;line-height:17px;margin-top:4px}
.quote{position:absolute;top:932px;width:174px;height:81px;border:2px solid #dcdcdc;padding:9px 12px;font-size:10.5px;line-height:15.5px;font-style:italic;color:var(--text)}
.quote::after{content:"";position:absolute;left:42px;bottom:-10px;width:14px;height:14px;background:#fff;border-right:2px solid #dcdcdc;border-bottom:2px solid #dcdcdc;transform:skewX(-40deg) rotate(25deg)}
.person{position:absolute;top:1031px;display:flex;align-items:center;gap:10px}
.person .avatar{width:45px;height:45px;border-radius:50%;background:linear-gradient(#d7e6ef,#8a9aa7)}
.person b{display:block;color:var(--gold);font-size:10.5px;letter-spacing:.4px}
.person small{font-size:9.5px;color:#999}
.side-box{position:absolute;left:755px;width:213px;text-align:center}
.subscribe{top:138px;height:118px;background:var(--panel);padding:10px 17px}
.side-box h3{font-size:13px;font-weight:600;color:var(--navy)}
.side-box p{font-size:9.5px;line-height:14px;margin-top:6px}
.email{display:flex;margin-top:11px;height:31px}
.email span{flex:1;background:#fff;border:1px solid #ccc;font-size:10px;color:#888;text-align:left;padding:0 11px;line-height:29px}
.email b{width:32px;background:var(--gold);color:#fff;font-size:9.5px;line-height:31px}
.booking{position:absolute;left:755px;top:265px;width:213px;height:389px;background:var(--gold-deep)}
.booking .head{background:var(--gold);height:97px;padding:12px 16px;color:#fff}
.booking h3{font-size:14.5px;font-weight:400;line-height:18px}
.booking .head p{font-size:10.5px;line-height:14px;margin-top:8px}
.booking form{padding:16px 17px 0}
.field{height:26px;background:var(--gold-field);border:1px solid var(--gold-line);color:#e5b44a;font-size:10px;line-height:24px;padding:0 9px;margin-bottom:5px}
.label{color:#fff;font-size:10.5px;margin:10px 0 5px}
.select{position:relative}
.select i{position:absolute;right:2px;top:2px;width:20px;height:20px;background:var(--navy)}
.select i::after{content:"";position:absolute;left:8px;top:9px;border:2px solid transparent;border-top-color:#fff}
.textarea{height:58px}
.submit{margin-top:8px;height:26px;background:#fff;border:1px solid #ddd;color:var(--navy);font-size:10.5px;font-weight:700;text-align:center;line-height:24px;letter-spacing:.4px}
.news{top:664px;height:126px;background:var(--panel);padding:11px 17px}
.news small{display:block;color:var(--gold);font-size:8px;margin-top:3px}
.btn{display:block;margin:9px auto 0;width:156px;height:26px;font-size:11px;font-weight:700;line-height:26px;letter-spacing:.3px}
.news .btn{background:var(--gold);color:#fff}
.patients{top:800px;height:114px;background:linear-gradient(var(--gold-light),var(--gold));padding:9px 17px;color:#fff}
.patients h3{color:#fff}
.patients .btn{background:#fff;color:var(--navy);border:1px solid #ddd}
.footer{position:absolute;left:0;top:1105px;width:1117px;height:59px;background:var(--navy);color:#fff;text-align:center;font-size:9.5px;line-height:14px;padding-top:15px}
.bottom-nav{position:absolute;left:0;top:1164px;width:1117px;height:36px;background:var(--navy-deep);display:flex;justify-content:center;gap:23px;color:#fff;font-size:10.5px;line-height:36px;letter-spacing:.3px}
</style>
</head>
<body>
<div class="topline"></div>
<header class="header">
  <div class="brand">Dr.med. Lukas M. Berger<br>Orthopädie und Orthopädische Chirurgie<br>Sportmedizin - Chirotherapie</div>
  <div class="social" aria-label="Social links"><span></span><span></span><span></span></div>
  <div class="call"><em>Call Now</em>+43 662 480 215</div>
  <div class="login">LOGIN</div>
</header>
<nav class="nav"><ul>
  <li class="active" style="width:63px">HOME</li>
  <li style="width:149px">ABOUT THE PRACTICE</li>
  <li style="width:132px">POWER SPECTRUM</li>
  <li style="width:157px">PATIENT INFORMATION</li>
  <li style="width:59px">NEWS</li>
  <li style="width:79px">CONTACT</li>
  <li style="width:125px">HOW TO FIND US</li>
  <li style="width:74px">IMPRINT</li>
</ul></nav>
<div class="goldbar"></div>
<main class="main"></main>

<div class="hero" role="img" aria-label="Photo: doctor examining a patient's knee"></div>
<div class="hero-card">
  <h2>Absolute <span>experience</span> you can trust</h2>
  <p>Lorem ipsum dolor sit amet, consectetur adipiscing elit. Morbi magna tellus, viverra ut dolor eu, luctus ultricies augue. Sed dignissim dolor tortor, ut pulvinar urna tristique vitae.</p>
  <a>Read more &gt;</a>
</div>

<section class="welcome">
  <h1>Welcome to orthopedics Dr.Berger</h1>
  <p>Mit dieser Internetseite stellen wir Ihnen eine Informationsplattform rund um unsere Arztpraxis bereit. Im Rahmen unserer fachärztlich orthopädischen Tätigkeit bieten wir ein breites Spektrum sowohl "schulmedizinischer" als auch "komplementärmedizinischer" Methoden von der Untersuchung über manuelle Therapieformen, diversen Injektionstechniken bis hin zu den aktuellen, auch minimalinvasiven Techniken der modernen orthopädischen Chirurgie an. Lernen Sie hier unsere Leistungen und unser Praxis-Team kennen.</p>
</section>

<h2 class="services-title">Our Services</h2>
<div class="services"></div>
<svg class="arrow" style="left:165px" width="30" height="30" viewBox="0 0 30 30"><circle cx="15" cy="15" r="13.5" fill="#fff" stroke="#d99c0e" stroke-width="2"/><path d="M18 8 L10 15 L18 22 Z" fill="#d99c0e"/></svg>
<svg class="arrow" style="left:716px" width="30" height="30" viewBox="0 0 30 30"><circle cx="15" cy="15" r="13.5" fill="#fff" stroke="#d99c0e" stroke-width="2"/><path d="M12 8 L20 15 L12 22 Z" fill="#d99c0e"/></svg>
<article class="service" style="left:219px">
  <div class="photo"><div role="img" aria-label="Photo: doctor with a spine model" style="background:linear-gradient(90deg,#c9c2b8,#e8e4df 60%,#d8c29a)"></div></div>
  <h3>SERVICE NAME</h3>
  <p>Lorem ipsum dolor sit amet, consectetur adipiscing elit. Morbi magna tellus, viverra ut dolor eu, luctus ultricies augue. Sed dignissim dolor tortor, ut pulvinar urna tristique vitae.</p>
  <a>Read More &gt;</a>
</article>
<article class="service" style="left:464px">
  <div class="photo"><div role="img" aria-label="Photo: therapist treating a patient's back" style="background:linear-gradient(90deg,#2f9a86,#d9b49c 45%,#f1f1f1)"></div></div>
  <h3>SERVICE NAME</h3>
  <p>Lorem ipsum dolor sit amet, consectetur adipiscing elit. Morbi magna tellus, viverra ut dolor eu, luctus ultricies augue. Sed dignissim dolor tortor, ut pulvinar urna tristique vitae.</p>
  <a>Read More &gt;</a>
</article>

<section class="about">
  <h2>About Us</h2>
  <p>Nulla a faucibus nisl. Nullam sollicitudin venenatis orci pretium luctus. Vivamus efficitur ornare orci. Fusce et elit a nunc blandit ultrices et eget felis. Class aptent taciti sociosqu ad litora torquent per conubia nostra, per inceptos himenaeos. Pellentesque nisl elit, laoreet nec mollis sodales, elementum vel mauris. Pellentesque habitant morbi tristique senectus et netus et malesuada fames ac turpis egestas.</p>
</section>
<blockquote class="quote" style="left:587px">Lorem ipsum dolor sit amet, consectetur adipiscing elit. Ut sollicitudin blandit lectus et tempus.</blockquote>
<blockquote class="quote" style="left:794px">Lorem ipsum dolor sit amet, consectetur adipiscing elit. Ut sollicitudin blandit lectus et tempus.</blockquote>
<div class="person" style="left:587px"><div class="avatar" role="img" aria-label="Portrait photo"></div><div><b>Martin Keller</b><small>Lorem Ipsum Co.</small></div></div>
<div class="person" style="left:794px"><div class="avatar" role="img" aria-label="Portrait photo"></div><div><b>Thomas Huber</b><small>Lorem Ipsum Co.</small></div></div>

<aside>
  <div class="side-box subscribe">
    <h3>Subscribe the specials</h3>
    <p>Lorem ipsum dolor sit amet, consec tetur adipiscing elit morbi magna telus.</p>
    <div class="email"><span>Enter your email Id</span><b>GO</b></div>
  </div>
  <div class="booking">
    <div class="head">
      <h3>Book a FREE<br>30 Minutes Consultation</h3>
      <p>Call +43 662 480 215 or complete the form below:</p>
    </div>
    <form>
      <div class="field">Name</div>
      <div class="field">Email Address</div>
      <div class="field">Phone</div>
      <div class="label">I would like more information on:</div>
      <div class="field select">Please Select<i></i></div>
      <div class="label">Comments/Message</div>
      <div class="field textarea"></div>
      <div class="submit">SUBMIT</div>
    </form>
  </div>
  <div class="side-box news">
    <h3>News</h3>
    <p>Lorem ipsum dolor sit amet, consec tetur adipiscing elit morbi magna telus.</p>
    <small>Posted : 27-08-2014</small>
    <span class="btn">READ MORE NEWS</span>
  </div>
  <div class="side-box patients">
    <h3>Patients Information</h3>
    <p>Lorem ipsum dolor sit amet, consec tetur adipiscing elit morbi magna telus.</p>
    <span class="btn">READ MORE</span>
  </div>
</aside>

<footer class="footer">Copyright ©, Orthopädie Dr.Berger, All rights reserved<br>Privacy Policy &nbsp;•&nbsp; Terms &amp; Condition</footer>
<nav class="bottom-nav"><span>Home</span><span>About the practice</span><span>power spectrum</span><span>patient Information</span><span>News</span><span>contact</span><span>How to find us</span><span>imprint</span></nav>
</body>
</html>
```